Modern Business Cards and Stationary for a Dentist
Derek M. Thalby, DDS, PLLC
Modern Business Cards and Stationary for a Dentist - Health
Creative Brief
Professional
Derek M. Thalby, DDS and Joanne R. Thalby, DDS
General Dentistry
318 West Brannig Street Fredericksburg, TX 78539
thalbydds@mailvesta.com
I need business cards and letterhead. There are two doctors in the office, please put both names on the business cards. They do not need separate cards. Please put the phone number for After Hours underneath the fax number. That number is 830-555-4172. I would like the front of the card to be colorful. But I would like the back of the card to be predominately white with color accents so that it is easy to read once the appointment information is written on it. Please try to incorporate the logo on the back as well.
Appointment card on the back. Line for the name. Under the line "Has an appointment on" then checkboxes for days of the week M,T,W,Th,F. Then another line for the Date and Time of the appointment and another line for Notes. Underneath everything the sentence: If you are unable to keep this appointment, please notify us within 24 hours.

```html
<!DOCTYPE html>
<html lang="en">
<head>
<meta charset="utf-8">
<title>Derek M. Thalby, DDS, PLLC — Stationery Set</title>
<link rel="stylesheet" href="https://fonts.googleapis.com/css2?family=Cinzel:wght@400;600&family=Open+Sans:ital,wght@0,400;0,600;1,400&display=swap">
<style>
  :root {
    --maroon: #7a1d3a;
    --maroon-dark: #5e1229;
    --gray: #9a9a9c;
    --gray-light: #cfcfd1;
    --ink: #4a4a4c;
    --paper: #ffffff;
    --backdrop: #e8e8e9;
  }
  * { margin: 0; padding: 0; box-sizing: border-box; }
  html, body { width: 1200px; height: 936px; overflow: hidden; }
  body {
    background: var(--backdrop);
    position: relative;
    font-family: "Open Sans", Arial, sans-serif;
    color: var(--ink);
  }
  .piece { position: absolute; background: var(--paper); overflow: hidden; }
  .piece > svg.art { position: absolute; left: 0; top: 0; }
  .brand { display: flex; align-items: center; gap: 6px; position: absolute; }
  .brand-dot { border-radius: 50%; background: var(--maroon); flex: none; }
  .brand-name { font-family: "Cinzel", Georgia, serif; font-weight: 600; color: var(--maroon); white-space: nowrap; }

  /* Letterhead */
  .letterhead { left: 183px; top: 68px; width: 390px; height: 549px; }
  .letterhead .brand { left: 40px; top: 22px; }
  .letterhead .brand-dot { width: 14px; height: 14px; }
  .letterhead .brand-name { font-size: 10px; }
  .lh-contact { position: absolute; right: 16px; top: 20px; font-size: 5px; line-height: 1.55; text-align: left; width: 110px; }
  .lh-body { position: absolute; left: 44px; top: 100px; width: 310px; font-size: 5.6px; line-height: 1.6; }
  .lh-body p { margin-bottom: 9px; }
  .lh-sign { position: absolute; left: 44px; top: 400px; font-size: 5.6px; line-height: 1.6; }
  .lh-sign .sig-space { height: 16px; }

  /* Folder */
  .folder { left: 634px; top: 43px; width: 426px; height: 579px; }
  .folder .brand { left: 0; right: 0; top: 236px; justify-content: center; flex-direction: column; gap: 10px; }
  .folder .brand-dot { width: 34px; height: 34px; }
  .folder .brand-name { font-size: 19px; font-weight: 400; }
  .folder-tagline { position: absolute; left: 0; right: 0; top: 318px; text-align: center; font-size: 11px; color: var(--maroon); letter-spacing: 0.2px; }
  .folder-web { position: absolute; left: 0; right: 0; top: 530px; text-align: center; font-family: "Cinzel", Georgia, serif; font-size: 13px; letter-spacing: 1.5px; color: #fff; }

  /* Business card front */
  .card-front { left: 38px; top: 665px; width: 195px; height: 109px; }
  .card-front .brand { left: 92px; top: 40px; flex-direction: column; gap: 3px; align-items: flex-start; }
  .card-front .brand-dot { width: 10px; height: 10px; }
  .card-front .brand-name { font-size: 6.6px; }
  .cf-details { position: absolute; left: 92px; top: 66px; font-size: 3.8px; line-height: 1.5; }

  /* Appointment card */
  .card-back { left: 38px; top: 784px; width: 195px; height: 116px; padding: 8px 12px; font-size: 4.6px; }
  .cb-title { font-weight: 600; color: var(--maroon); font-size: 6px; margin-bottom: 7px; }
  .cb-line { border-bottom: 0.6px solid var(--gray); height: 9px; margin-bottom: 4px; display: flex; align-items: flex-end; }
  .cb-label { margin-bottom: 3px; }
  .cb-days { display: flex; gap: 9px; margin-bottom: 4px; }
  .cb-day { display: flex; align-items: center; gap: 2px; }
  .cb-box { width: 5px; height: 5px; border: 0.6px solid var(--maroon); }
  .cb-note { margin-top: 7px; font-style: italic; color: var(--maroon); font-size: 4.2px; }
  .cb-brand { position: absolute; right: 10px; top: 8px; display: flex; align-items: center; gap: 3px; }
  .cb-brand .brand-dot { width: 6px; height: 6px; }
  .cb-brand .brand-name { font-size: 4.4px; }

  /* Envelopes */
  .envelope-front { left: 264px; top: 672px; width: 416px; height: 211px; }
  .envelope-front .brand { left: 34px; top: 22px; }
  .envelope-front .brand-dot { width: 12px; height: 12px; }
  .envelope-front .brand-name { font-size: 9px; }
  .env-address { position: absolute; left: 52px; top: 40px; font-size: 5px; line-height: 1.5; }
  .envelope-back { left: 738px; top: 672px; width: 421px; height: 216px; }
</style>
</head>
<body>

<!-- Letterhead -->
<section class="piece letterhead">
  <svg class="art" width="390" height="549" viewBox="0 0 390 549">
    <path d="M0 0 H22 C30 150 30 400 14 549 H0 Z" fill="var(--maroon)"/>
    <path d="M26 0 C34 150 34 400 18 549" fill="none" stroke="var(--gray)" stroke-width="2"/>
  </svg>
  <div class="brand"><span class="brand-dot"></span><span class="brand-name">Derek M. Thalby, DDS, PLLC</span></div>
  <div class="lh-contact">
    318 West Brannig Street<br>
    Fredericksburg, TX 78539<br>
    Tel: 830-555-4160<br>
    Fax: 830-555-4190<br>
    After Hours: 830-555-4172<br>
    thalbydds@mailvesta.com
  </div>
  <div class="lh-body">
    <p>June 9, 2014</p>
    <p>Dear Patient,</p>
    <p>Thank you for choosing our practice for your dental care. We are pleased to welcome you and your family, and we look forward to helping you keep a healthy, confident smile for many years to come.</p>
    <p>Our team offers general dentistry in a calm, friendly setting. Each visit begins with a careful exam, a gentle cleaning and a clear plan that fits your needs and your schedule.</p>
    <p>Please call our office if you have any questions before your first appointment. We are always happy to help, and we thank you for the trust you place in us.</p>
    <p>Best Regards,</p>
  </div>
  <div class="lh-sign">
    <div class="sig-space"></div>
    <strong>Derek M. Thalby, DDS</strong><br>
    Dentist<br>
    318 West Brannig Street, Fredericksburg, TX 78539
  </div>
</section>

<!-- Presentation folder -->
<section class="piece folder">
  <svg class="art" width="426" height="579" viewBox="0 0 426 579">
    <path d="M0 420 C120 440 280 420 426 360 V379 C280 440 120 458 0 440 Z" fill="var(--gray-light)"/>
    <path d="M0 436 C120 452 280 432 426 372 V386 C280 446 120 466 0 452 Z" fill="var(--gray)"/>
    <path d="M0 456 C120 470 280 452 426 392 V579 H0 Z" fill="var(--maroon)"/>
  </svg>
  <div class="brand"><span class="brand-dot"></span><span class="brand-name">Derek M. Thalby, DDS, PLLC</span></div>
  <div class="folder-tagline">Gentle Care.. Bright Smiles, Close to Home..</div>
  <div class="folder-web">www.ThalbySmiles.com</div>
</section>

<!-- Business card front -->
<section class="piece card-front">
  <svg class="art" width="195" height="109" viewBox="0 0 195 109">
    <path d="M0 0 H70 C62 40 66 75 80 109 H0 Z" fill="var(--maroon)"/>
    <path d="M74 0 C66 40 70 75 84 109" fill="none" stroke="var(--gray)" stroke-width="2"/>
  </svg>
  <div class="brand"><span class="brand-dot"></span><span class="brand-name">Derek M. Thalby, DDS, PLLC</span></div>
  <div class="cf-details">
    Derek M. Thalby, DDS &nbsp;·&nbsp; Joanne R. Thalby, DDS<br>
    318 West Brannig Street, Fredericksburg, TX 78539<br>
    Tel: 830-555-4160 &nbsp; Fax: 830-555-4190<br>
    After Hours: 830-555-4172<br>
    thalbydds@mailvesta.com
  </div>
</section>

<!-- Appointment card -->
<section class="piece card-back">
  <svg class="art" width="195" height="116" viewBox="0 0 195 116">
    <rect x="0" y="0" width="4" height="116" fill="var(--maroon)"/>
  </svg>
  <div class="cb-brand"><span class="brand-dot"></span><span class="brand-name">Derek M. Thalby, DDS</span></div>
  <div class="cb-title">Appointment</div>
  <div class="cb-line">Name</div>
  <div class="cb-label">Has an appointment on</div>
  <div class="cb-days">
    <span class="cb-day"><span class="cb-box"></span>M</span>
    <span class="cb-day"><span class="cb-box"></span>T</span>
    <span class="cb-day"><span class="cb-box"></span>W</span>
    <span class="cb-day"><span class="cb-box"></span>Th</span>
    <span class="cb-day"><span class="cb-box"></span>F</span>
  </div>
  <div class="cb-line">Date &amp; Time</div>
  <div class="cb-line">Notes</div>
  <div class="cb-note">If you are unable to keep this appointment, please notify us within 24 hours.</div>
</section>

<!-- Envelope front -->
<section class="piece envelope-front">
  <svg class="art" width="416" height="211" viewBox="0 0 416 211">
    <path d="M0 0 H14 C24 70 24 140 10 211 H0 Z" fill="var(--maroon)"/>
    <path d="M18 0 C28 70 28 140 14 211" fill="none" stroke="var(--gray)" stroke-width="2"/>
  </svg>
  <div class="brand"><span class="brand-dot"></span><span class="brand-name">Derek M. Thalby, DDS, PLLC</span></div>
  <div class="env-address">318 West Brannig Street, Fredericksburg, TX 78539</div>
</section>

<!-- Envelope back -->
<section class="piece envelope-back">
  <svg class="art" width="421" height="216" viewBox="0 0 421 216">
    <path d="M2 2 L210 110 L419 2" fill="none" stroke="var(--gray-light)" stroke-width="1.5"/>
    <path d="M0 216 L180 96 M421 216 L240 96" fill="none" stroke="#e4e4e5" stroke-width="1"/>
  </svg>
</section>

</body>
</html>
```